Email Signatures

I would like to create a new email signature for my team. The design will be the same for everyone, with only individual details such as name and email changing. You can also see our brand style on our website. https://www.tlmbespokehomes.com.au/

Target Market(s)

Clients for new builds or renovations

Industry/Entity Type

Construction

Colors

Designer to choose colors to be used in the design.

```html
<!DOCTYPE html>
<html lang="en">
<head>
<meta charset="utf-8">
<title>TLM Bespoke Homes – Email Signature</title>
<link rel="stylesheet" href="https://fonts.googleapis.com/css2?family=Work+Sans:wght@400;500;600&display=swap">
<style>
  :root {
    --stage: #4a3426;
    --card: #ffffff;
    --green: #2e9b47;
    --band-green: #30aa4a;
    --ink: #333333;
    --dark: #231f20;
    --logo-dark: #352f2d;
    --rule: #dddddd;
    --gold: #c99a3a;
    --silver: #b9babc;
    --black: #1e1e1e;
    --orange: #f6a21c;
    --blue: #2a55a6;
  }
  * { box-sizing: border-box; margin: 0; padding: 0; }
  html, body { width: 1200px; height: 1200px; overflow: hidden; }
  body {
    background: var(--stage);
    font-family: "Work Sans", sans-serif;
    color: var(--ink);
    position: relative;
  }
  .signature {
    position: absolute;
    left: 86px; top: 247px;
    width: 1040px; height: 659px;
    background: var(--card);
    overflow: hidden;
  }
  .brand-mark {
    position: absolute;
    left: 46px; top: 47px;
    width: 304px; height: 304px;
    border-radius: 50%;
    background: var(--logo-dark);
    display: flex; align-items: center; justify-content: center;
    text-align: center;
    color: #ffffff;
    font-weight: 500;
    font-size: 34px;
    line-height: 1.2;
    letter-spacing: 1px;
  }
  .identity {
    position: absolute; left: 411px; top: 60px;
    white-space: nowrap;
  }
  .identity .person { color: var(--green); font-weight: 600; font-size: 28px; }
  .identity .role { color: var(--ink); font-weight: 500; font-size: 20px; margin-left: 6px; }
  .rule {
    position: absolute; left: 411px; width: 518px; height: 1px;
    background: var(--rule);
  }
  .rule.top { top: 115px; }
  .rule.bottom { top: 277px; }
  .contact-line {
    position: absolute; left: 406px;
    display: flex; align-items: center; gap: 12px;
    font-size: 20px; font-weight: 500; white-space: nowrap;
  }
  .contact-line svg { width: 24px; height: 24px; flex: none; }
  .contact-line.phone { top: 135px; font-size: 21px; }
  .contact-line.email { top: 184px; }
  .contact-line.location { top: 232px; }
  .social-row {
    position: absolute; left: 410px; top: 300px;
    display: flex; align-items: center;
    font-size: 18px; font-weight: 500;
  }
  .social-item { display: flex; align-items: center; gap: 8px; }
  .social-item .dot {
    width: 30px; height: 30px; border-radius: 50%;
    border: 1.5px solid var(--green);
  }
  .social-divider { width: 1px; height: 26px; background: var(--rule); margin: 0 14px; }
  .awards {
    position: absolute; left: 51px; top: 406px;
    display: flex; gap: 10px;
  }
  .award {
    width: 84px; height: 84px; border-radius: 50%;
    margin-right: 0;
  }
  .award.gold { background: radial-gradient(circle, #e0b45a, var(--gold)); }
  .award.black { background: radial-gradient(circle, #3a3a3a, var(--black)); border: 3px solid #bbb; }
  .award.silver { background: radial-gradient(circle, #d8d9db, var(--silver)); }
  .award.orange { background: radial-gradient(circle, #ffc247, var(--orange)); }
  .award.blue { background: radial-gradient(circle, #ffffff 55%, var(--blue) 60%); border: 3px solid #c8cdd6; }
  .footer-band { position: absolute; left: 0; top: 0; width: 1040px; height: 659px; }
  .website {
    position: absolute; left: 533px; top: 600px;
    color: #ffffff; font-size: 25px; font-weight: 500;
  }
</style>
</head>
<body>
  <main class="signature">
    <div class="brand-mark">TLM<br>Bespoke Homes</div>

    <div class="identity">
      <span class="person">Liam Hartley,</span><span class="role">General Manager</span>
    </div>
    <div class="rule top"></div>

    <div class="contact-line phone">
      <svg viewBox="0 0 24 24" fill="none" stroke="var(--green)" stroke-width="1.6"><circle cx="12" cy="12" r="10.5"/><path d="M9 6.5c-1.5 1-2 3-1 5.5s2.8 4.6 5 5.4c1 .3 1.8 0 2.3-.7l-1.8-2-1.4.8c-1-.6-2-2-2.3-3.3l1.2-1-1-2.7z" fill="var(--green)" stroke="none"/></svg>
      <span>0400 555 018</span>
    </div>
    <div class="contact-line email">
      <svg viewBox="0 0 24 24"><path d="M2 9l10-6 10 6v11H2z" fill="var(--green)"/><path d="M2 9l10 7 10-7" fill="none" stroke="#fff" stroke-width="1.4"/><rect x="7" y="6" width="10" height="5" fill="#fff"/></svg>
      <span>info@tlmbespokehomes.com.au</span>
    </div>
    <div class="contact-line location">
      <svg viewBox="0 0 24 24"><path d="M12 1.5a7 7 0 0 0-7 7c0 5 7 14 7 14s7-9 7-14a7 7 0 0 0-7-7z" fill="var(--green)"/><circle cx="12" cy="8.5" r="2.6" fill="#fff"/></svg>
      <span>Hobart, Tasmania Australia</span>
    </div>
    <div class="rule bottom"></div>

    <div class="social-row">
      <div class="social-item"><span class="dot"></span><span>Reviews</span></div>
      <span class="social-divider" style="margin-left:28px;margin-right:12px"></span>
      <div class="social-item"><span class="dot"></span><span>Network</span></div>
      <span class="social-divider" style="margin-left:32px;margin-right:20px"></span>
      <div class="social-item"><span class="dot"></span><span>Updates</span></div>
      <span class="social-divider" style="margin-left:14px;margin-right:22px"></span>
      <div class="social-item"><span class="dot"></span><span>Gallery</span></div>
    </div>

    <div class="awards" aria-label="Industry award badges">
      <span class="award gold"></span>
      <span class="award black"></span>
      <span class="award silver"></span>
      <span class="award gold"></span>
      <span class="award gold"></span>
      <span class="award black"></span>
      <span class="award silver"></span>
      <span class="award orange"></span>
      <span class="award black" style="margin-left:6px"></span>
      <span class="award blue" style="margin-left:10px;width:96px;height:96px;margin-top:-6px"></span>
    </div>

    <svg class="footer-band" viewBox="0 0 1040 659" aria-hidden="true">
      <polygon points="0,633 837,532 1040,634 1040,659 0,659" fill="var(--band-green)"/>
      <polygon points="0,645 837,549 1036,652 1036,659 0,659" fill="var(--dark)"/>
    </svg>
    <div class="website">www.tlmbespokehomes.com.au</div>
  </main>
</body>
</html>
```